Criação de Papelaria (6 itens) para Arquitetura
" Está sendo concluída a fábrica dos revestimentos, que será a responsável pela produção de todos os produtos 3D: painéis, murais, cobogós e imitações em pedra, em sua maioria fabricados em gesso especial, exclusivo da Ventra Relevo "

```html
<!DOCTYPE html>
<html lang="pt-BR">
<head>
<meta charset="UTF-8">
<title>Ventra Relevo — Envelope</title>
<link rel="stylesheet" href="https://fonts.googleapis.com/css2?family=Montserrat:wght@400;600;800&display=swap">
<style>
  :root {
    --page-bg: #e9eaed;
    --paper: #ffffff;
    --navy-deep: #0a1560;
    --navy: #1a2a8c;
    --royal: #2c43b8;
    --ink: #1b2340;
    --muted: #5a6275;
    --silver-light: #eef0f4;
    --silver-dark: #9aa0ad;
  }
  * { margin: 0; padding: 0; box-sizing: border-box; }
  html, body {
    width: 1200px; height: 1200px; overflow: hidden;
    background: var(--page-bg);
    font-family: "Montserrat", Arial, sans-serif;
  }
  .stationery {
    position: relative; width: 1200px; height: 1200px;
  }
  .envelope {
    position: absolute; top: 215px; width: 500px; height: 770px;
    box-shadow: 0 10px 30px rgba(0,0,0,0.28);
    overflow: hidden;
  }
  /* Front */
  .envelope--front { left: 80px; background: var(--paper); }
  .envelope__flap { position: absolute; top: 0; left: 0; width: 500px; height: 90px; }
  .contact {
    position: absolute; left: 30px; bottom: 40px;
    font-size: 9px; color: var(--muted); line-height: 1.35;
  }
  .contact__row { display: flex; align-items: center; gap: 8px; margin-top: 12px; }
  .contact__row:first-child { margin-top: 0; }
  .contact__icon {
    width: 12px; height: 12px; border-radius: 50%;
    background: var(--navy); flex-shrink: 0;
  }
  .front-brand {
    position: absolute; right: 30px; bottom: 42px;
    display: flex; align-items: center; gap: 8px;
    font-weight: 800; font-size: 20px; color: var(--navy);
  }
  .brand-mark { width: 14px; height: 14px; border-radius: 50%; background: var(--navy); }
  /* Back */
  .envelope--back {
    left: 620px;
    background: radial-gradient(ellipse at 50% 40%, var(--royal) 0%, var(--navy) 45%, var(--navy-deep) 100%);
  }
  .back-brand {
    position: absolute; top: 330px; left: 0; width: 100%;
    display: flex; justify-content: center; align-items: center; gap: 12px;
    font-weight: 800; font-size: 40px; color: var(--silver-light);
  }
  .back-brand .brand-mark { width: 22px; height: 22px; background: var(--silver-light); }
  .envelope__band {
    position: absolute; left: 0; bottom: 0; width: 100%; height: 26px;
    background: linear-gradient(180deg, var(--silver-light) 0%, var(--silver-dark) 100%);
  }
</style>
</head>
<body>
<main class="stationery">
  <section class="envelope envelope--front" aria-label="Envelope frente">
    <svg class="envelope__flap" viewBox="0 0 500 90" preserveAspectRatio="none" aria-hidden="true">
      <defs>
        <linearGradient id="flapFill" x1="0" y1="0" x2="1" y2="0">
          <stop offset="0" stop-color="#0a1560"/>
          <stop offset="0.5" stop-color="#2c43b8"/>
          <stop offset="1" stop-color="#0a1560"/>
        </linearGradient>
      </defs>
      <path d="M0 0 H500 V40 Q500 80 455 80 H45 Q0 80 0 40 Z" fill="url(#flapFill)"/>
    </svg>

    <div class="contact">
      <div class="contact__row">
        <span class="contact__icon"></span>
        <span>(11) 4000-1234<br>(11) 4000-5678</span>
      </div>
      <div class="contact__row">
        <span class="contact__icon"></span>
        <span>www.ventrarelevo.com</span>
      </div>
      <div class="contact__row">
        <span class="contact__icon"></span>
        <span>R. das Pedras, 120 - Bairro<br>CEP 00000-000 - Cidade</span>
      </div>
    </div>

    <div class="front-brand"><span class="brand-mark"></span>Ventra Relevo</div>
  </section>

  <section class="envelope envelope--back" aria-label="Envelope verso">
    <div class="back-brand"><span class="brand-mark"></span>Ventra Relevo</div>
    <div class="envelope__band"></div>
  </section>
</main>
</body>
</html>
```